Professional Photography Business cards

I need business cards that include my logo which I have uploaded. I run a photography business. I am open to ideas but I would like one side to have my logo and the other side to have my contact info. I don't have a website made but I do own a website domain. I have uploaded 2 different logo color schemes. My business colors are Blue, black , and white.

Business Name
Business Phone Number
Business Email
Business Website address
Instagram

Industry/Entity Type

Professional Photography

Contact Information for Business Card

Phone Number: 555-314-8027 email: info@tkellan-studios.example Instagram: @t.kellanstudios website doman- www.tkellan-studios.example

Requirements
Must have
• I like the idea of a business card with a full black background front and back of card. My colors must include royal blue, black, and white

```html
<!DOCTYPE html>
<html lang="en">
<head>
<meta charset="UTF-8">
<title>T. Kellan Studios — Business Card</title>
<link href="https://fonts.googleapis.com/css2?family=Playfair+Display:wght@400&display=swap" rel="stylesheet">
<style>
  :root {
    --backdrop: #1c1c1c;
    --royal-blue: #2b3190;
    --paper: #ffffff;
    --ink: #111111;
    --faint-on-blue: rgba(255, 255, 255, 0.16);
    --faint-on-white: #e4e4e4;
  }
  * { margin: 0; padding: 0; box-sizing: border-box; }
  html, body {
    width: 1200px;
    height: 1200px;
    overflow: hidden;
    background: var(--backdrop);
    font-family: "Playfair Display", Georgia, serif;
  }
  .stage { position: relative; width: 1200px; height: 1200px; }
  .card {
    position: absolute;
    width: 462px;
    height: 714px;
    overflow: hidden;
  }
  .card--front { left: 128px; top: 202px; background: var(--royal-blue); }
  .card--back { left: 638px; top: 325px; background: var(--paper); }

  .faint-mark {
    position: absolute;
    width: 112px;
    height: 112px;
    border-radius: 50%;
    border: 7px solid var(--faint-on-blue);
  }
  .card--front .faint-mark { left: 173px; top: 104px; }
  .card--back .faint-mark { left: 258px; top: 557px; border-color: var(--faint-on-white); }

  .brand {
    position: absolute;
    left: 0;
    width: 100%;
    display: flex;
    align-items: center;
    justify-content: center;
    gap: 14px;
    font-size: 34px;
    font-weight: 400;
    white-space: nowrap;
  }
  .card--front .brand { top: 358px; color: var(--paper); }
  .card--back .brand { top: 94px; color: var(--royal-blue); font-size: 32px; }
  .brand__dot {
    width: 44px;
    height: 44px;
    border-radius: 50%;
    border: 4px solid currentColor;
    flex: none;
  }

  .contact-list {
    position: absolute;
    left: 0;
    top: 0;
    width: 100%;
    list-style: none;
  }
  .contact-item {
    position: absolute;
    left: 0;
    width: 100%;
    display: flex;
    align-items: center;
    justify-content: center;
    gap: 12px;
    color: var(--ink);
    font-size: 20px;
    white-space: nowrap;
  }
  .contact-item--phone { top: 260px; font-size: 30px; gap: 14px; }
  .contact-item--email { top: 328px; }
  .contact-item--social { top: 390px; }
  .contact-item--web { top: 446px; }
  .contact-icon { width: 20px; height: 20px; flex: none; }
  .contact-item--phone .contact-icon { width: 24px; height: 24px; }
  .social-square {
    width: 18px;
    height: 18px;
    border: 2px solid var(--royal-blue);
    border-radius: 4px;
    flex: none;
  }
</style>
</head>
<body>
<main class="stage">
  <section class="card card--front" aria-label="Card front">
    <div class="faint-mark" aria-hidden="true"></div>
    <div class="brand"><span class="brand__dot" aria-hidden="true"></span>T. Kellan Studios</div>
  </section>

  <section class="card card--back" aria-label="Card back">
    <div class="brand"><span class="brand__dot" aria-hidden="true"></span>T. Kellan Studios</div>
    <ul class="contact-list">
      <li class="contact-item contact-item--phone">
        <svg class="contact-icon" viewBox="0 0 24 24" fill="none" stroke="#2b3190" stroke-width="1.4" stroke-linejoin="round" aria-hidden="true">
          <path d="M5 3h4l2 5-2.5 1.5a11 11 0 0 0 6 6L16 13l5 2v4a2 2 0 0 1-2 2A16 16 0 0 1 3 5a2 2 0 0 1 2-2z"/>
          <path d="M15 3a6 6 0 0 1 6 6M15 6a3 3 0 0 1 3 3"/>
        </svg>
        <span>555-314-8027</span>
      </li>
      <li class="contact-item contact-item--email">
        <svg class="contact-icon" viewBox="0 0 24 24" fill="none" stroke="#2b3190" stroke-width="1.5" aria-hidden="true">
          <rect x="2" y="5" width="20" height="14"/>
          <path d="M2 5l10 8 10-8M2 19l7-7M22 19l-7-7"/>
        </svg>
        <span>info@tkellan-studios.example</span>
      </li>
      <li class="contact-item contact-item--social">
        <span class="social-square" aria-hidden="true"></span>
        <span>@t.kellanstudios</span>
      </li>
      <li class="contact-item contact-item--web">
        <svg class="contact-icon" viewBox="0 0 24 24" fill="none" stroke="#2b3190" stroke-width="1.5" aria-hidden="true">
          <circle cx="12" cy="12" r="9"/>
          <ellipse cx="12" cy="12" rx="4" ry="9"/>
          <path d="M3 12h18M5 7h14M5 17h14"/>
        </svg>
        <span>www.tkellan-studios.example</span>
      </li>
    </ul>
    <div class="faint-mark" aria-hidden="true"></div>
  </section>
</main>
</body>
</html>
```